Web Design Project

We need a web design for a new company that we started called TALMO CNG. TALMO CNG is a company that will build, own and operate compressed natural gas fueling stations throughout the United States. Our primary customers are Trucking companies and the stations will be built for semi trucks. CNG is better for the environment than diesel fuel, and will save trucking companies loads of money. It is also a domestic product which means that it will create American jobs and help America become energy independent. I have attached a logo that we are using. We dont need to stay with this logo persay, but it is what we have for now. We have a video on Youtube that shows a bit of what we are doing. just search for TALMO CNG. TALMO CNG is a sister company of Haulbright of Arizona,www.hbrtqx.example and a nationwide distributor of VANTO RIG, www.vantorig.example. We will need links to these sites. Please make any pictures of trucks Haulbright trucks, and please do not use pictures of cabover trucks.

Target Market(s)

The target market are truck drivers and truckers.

Industry/Entity Type

Environment

Requirements
Must have
• Map showing station locations, a page with industry news, a page with a savings calculator (we can code the calculator) Site should have links to

```html
<!DOCTYPE html>
<html lang="en">
<head>
<meta charset="utf-8">
<title>TALMO CNG</title>
<link href="https://fonts.googleapis.com/css2?family=Carlito:wght@400;700&family=Arimo:wght@400&display=swap" rel="stylesheet">
<style>
:root{
  --green:#05ee3d;
  --green-text:#0ce63a;
  --footer-top:#2fb82c;
  --footer-bottom:#0c8f12;
  --teal:#1fa3b3;
  --teal-dark:#138896;
  --ink:#444;
  --ink-soft:#555;
  --line:#d7d7d7;
  --card:#f1f1f1;
}
*{margin:0;padding:0;box-sizing:border-box}
html,body{width:1143px;height:1200px;overflow:hidden}
body{position:relative;font-family:"Carlito",sans-serif;color:var(--ink);
  background:linear-gradient(#fff 0,#ececec 340px,#f4f4f4 341px,#f4f4f4 512px,#fff 513px,#f6f6f6 870px,#fff 871px)}
.topbar{position:absolute;left:0;top:0;width:100%;height:4px;background:var(--green)}
.social{position:absolute;left:739px;top:9px;font-size:16px;color:#555;letter-spacing:.5px}
.social-btn{position:absolute;top:4px;width:40px;height:35px;background:var(--green)}
.social-btn span{position:absolute;left:13px;top:11px;width:14px;height:14px;background:#fff;border-radius:2px}
.brand{position:absolute;left:119px;top:40px;font-weight:700;font-size:58px;color:var(--green-text);letter-spacing:1px}
.nav-rule{position:absolute;left:438px;top:99px;width:676px;height:1px;background:var(--line)}
.nav-home{position:absolute;left:452px;top:90px;width:74px;height:43px;background:linear-gradient(var(--teal),var(--teal-dark))}
.nav a{position:absolute;top:106px;font-size:14px;color:#333;text-decoration:none;letter-spacing:.3px}
.nav a.active{color:#fff;left:469px}
.hero{position:absolute;left:103px;top:164px;width:680px;height:337px;border:1px solid #ccc;
  background:linear-gradient(110deg,#cfcfcf 0,#3fb84a 30%,#2f9e3d 55%,#8a8a8a 75%,#5a5a5a 100%)}
.calc{position:absolute;left:790px;top:163px;width:250px;height:338px;background:var(--green)}
.calc h2{position:absolute;left:5px;top:16px;font-size:20px;color:#fff;letter-spacing:.5px;white-space:nowrap}
.field{position:absolute;left:13px;width:222px;height:23px;background:#fff;border-radius:12px;font-size:11.5px;color:#777;padding:4px 14px}
.field svg{position:absolute;right:10px;top:8px}
.calc-btn{position:absolute;left:38px;top:278px;width:164px;height:27px;background:linear-gradient(#5a5a5a,#222);border:1px solid #fff;
  border-radius:3px;color:#fff;font-size:15px;text-align:center;line-height:25px;letter-spacing:1px}
.calc-btn::before,.calc-btn::after{content:"";position:absolute;top:0;width:20px;height:25px;background:#444;border-right:2px solid #ddd}
.calc-btn::before{left:0}.calc-btn::after{right:0;border-right:0;border-left:2px solid #ddd}
.card{position:absolute;top:530px;width:218px;height:313px;background:var(--card);border:1px solid #ddd;box-shadow:0 8px 8px -6px #999}
.card h3{position:absolute;left:18px;top:6px;font-weight:400;font-size:23px;color:#666}
.card .pic{position:absolute;left:13px;top:41px;width:193px;height:144px}
.card ul{position:absolute;left:12px;top:200px;width:182px;list-style:none}
.card li{height:28.5px;border-bottom:1px dotted #bbb;font-size:12px;color:#333;padding:4px 0 0 28px;position:relative}
.card li:last-child{border-bottom:0}
.card li::before{content:"";position:absolute;left:6px;top:5px;width:12px;height:12px;border-radius:50%;background:radial-gradient(var(--green) 40%,#ccc 45%)}
.card .lead{position:absolute;left:12px;top:200px;width:190px;border-bottom:1px dotted #bbb;font-size:12px;color:#333;padding:4px 0 8px 28px}
.card .lead::before{content:"";position:absolute;left:6px;top:5px;width:12px;height:12px;border-radius:50%;background:radial-gradient(var(--green) 40%,#ccc 45%)}
.card p{position:absolute;left:13px;top:232px;width:195px;font-size:11.5px;line-height:19px;text-align:justify;color:#333}
.more{position:absolute;right:0;bottom:0;width:116px;height:23px;background:linear-gradient(var(--teal),var(--teal-dark));
  border-top-left-radius:20px;color:#fff;font-weight:700;font-size:12.5px;text-align:center;line-height:23px}
.about h2{position:absolute;left:115px;top:882px;font-size:24px;color:var(--green-text);letter-spacing:1px}
.about .intro{position:absolute;left:116px;top:918px;width:900px;font-size:16.5px;line-height:23px;color:#555}
.about .col{position:absolute;top:972px;width:438px;font-size:10.5px;line-height:19px;text-align:justify;color:#444}
footer{position:absolute;left:0;top:1117px;width:100%;height:83px;background:linear-gradient(var(--footer-top),var(--footer-bottom));overflow:hidden}
.foot-badge{position:absolute;left:90px;top:-80px;width:183px;height:157px;border-radius:50%;background:#fff}
.foot-brand{position:absolute;left:110px;top:10px;font-weight:700;font-size:30px;color:var(--green-text)}
.foot-links{position:absolute;left:340px;width:540px;text-align:center;font-family:"Arimo",sans-serif;font-size:12px;color:#fff;word-spacing:2px}
.foot-links span{margin:0 8px}
</style>
</head>
<body>
<div class="topbar"></div>
<div class="social">Socialize With us :</div>
<div class="social-btn" style="left:871px"><span></span></div>
<div class="social-btn" style="left:915px"><span></span></div>
<div class="social-btn" style="left:959px"><span></span></div>
<div class="social-btn" style="left:1003px"><span></span></div>

<div class="brand">TALMO CNG</div>

<div class="nav-rule"></div>
<div class="nav-home"></div>
<nav class="nav">
  <a class="active" href="#">HOME</a>
  <a href="#" style="left:548px">ABOUT US</a>
  <a href="#" style="left:641px">TECHNOLOGY</a>
  <a href="#" style="left:763px">PRODUCTS</a>
  <a href="#" style="left:865px">CALCULATOR</a>
  <a href="#" style="left:979px">CONTACT</a>
</nav>

<div class="hero" role="img" aria-label="Green conventional semi truck with trailer on a mountain highway"></div>

<section class="calc">
  <h2>FUEL SAVING CALCULATOR</h2>
  <div class="field" style="top:65px">Select Any State<svg width="12" height="7"><path d="M0 0h12L6 7z" fill="#666"/></svg></div>
  <div class="field" style="top:107px">Annual Miles Per Tractor</div>
  <div class="field" style="top:148px">Annual Mpg</div>
  <div class="field" style="top:190px">Cng or Lng Preference<svg width="12" height="7"><path d="M0 0h12L6 7z" fill="#666"/></svg></div>
  <div class="field" style="top:231px">Annual Saving Per Tractor</div>
  <div class="calc-btn">CALCULATE</div>
</section>

<article class="card" style="left:106px">
  <h3>Location</h3>
  <div class="pic" role="img" aria-label="Street map of station locations" style="background:linear-gradient(135deg,#ece9df,#d9d4c3);border:1px solid #ccc"></div>
  <ul><li>Local</li><li>Long Distance</li><li>International</li></ul>
  <div class="more">More info&gt;&gt;</div>
</article>
<article class="card" style="left:348px">
  <h3 style="left:32px">Products</h3>
  <div class="pic" role="img" aria-label="Warehouse with stacked boxes and pallet jack" style="background:linear-gradient(135deg,#8a7a62,#c79a62 50%,#5d4a36)"></div>
  <ul><li>Certification</li><li>Date Sheets</li><li>Photo's</li></ul>
  <div class="more">More info&gt;&gt;</div>
</article>
<article class="card" style="left:591px">
  <h3 style="left:24px">Industry News</h3>
  <div class="pic" role="img" aria-label="Orange truck driving on a mountain road" style="background:linear-gradient(135deg,#6a86b0,#a58e74 50%,#5a5048)"></div>
  <div class="lead">Lorum ipsum is dummy text</div>
  <p>Lorem ipsum dolor sit amet, con tuer adipiscing elitaesent ves tibul-umie lacus Aenean.</p>
  <div class="more">More info&gt;&gt;</div>
</article>
<article class="card" style="left:822px">
  <h3 style="left:26px">Videos</h3>
  <div class="pic" style="left:16px;top:49px;width:188px;height:136px;background:#000">
    <svg width="188" height="136"><circle cx="94" cy="52" r="15" fill="none" stroke="#fff" stroke-width="3"/><path d="M89 44v16l13-8z" fill="#fff"/><rect x="0" y="122" width="188" height="14" fill="#333"/></svg>
  </div>
  <div class="lead">Lorum ipsum is dummy text</div>
  <p>Lorem ipsum dolor sit amet, con tuer adipiscing elitaesent ves tibul-umie lacus Aenean.</p>
  <div class="more">More info&gt;&gt;</div>
</article>

<section class="about">
  <h2>ABOUT US ?</h2>
  <p class="intro">The TALMO cng team has been designing, developing and selling natural gas systems for heavy trucks globally for more than 15 years.</p>
  <p class="col" style="left:115px">Lorem ipsum dolor sit amet, con tuer adipiscing elitaesent ves tibulumie lacus. Aenean my hendrerit is. Phasellus porta. Fusce suscipit varius mi. Cum sociis natoque penatibus et magnis dis parturient montes, nascetur ridiculus mus. Nulla dui. Fusce feugiat malesuada odio. Morbi nunc odio gravida at cursus necTibulumie lacus. Aenean my hendrerit is. Phasellus porta. Fusce suscipit varius mi.</p>
  <p class="col" style="left:584px">Lorem ipsum dolor sit amet, con tuer adipiscing elitaesent ves tibulumie lacus. Aenean my hendrerit is. Phasellus porta. Fusce suscipit varius mi. Cum sociis natoque penatibus et magnis dis parturient montes, nascetur ridiculus mus. Nulla dui. Fusce feugiat malesuada odio. Morbi nunc odio gravida at cursus necTibulumie lacus. Aenean my hendrerit is. Phasellus porta. Fusce suscipit varius mi.</p>
</section>

<footer>
  <div class="foot-badge"></div>
  <div class="foot-brand">TALMO CNG</div>
  <div class="foot-links" style="top:12px">Home<span>/</span>About us<span>/</span>Technology<span>/</span>Products<span>/</span>Location<span>/</span>News<span>/</span>Contact us</div>
  <div class="foot-links" style="top:35px">Privacy Policy<span>/</span>Terms of Use<span>/</span>Publisher Information<span>/</span>Articles &amp; Tips</div>
  <div class="foot-links" style="top:58px;left:335px;width:540px">© Talmo Cng 2013 | All Rights Reserved</div>
</footer>
</body>
</html>
```